Health & Wellness Contest - The Bright Harvest Renewal

We need a postcard design that is professional and grabs the attention of people who see it. The postcard will be left in fitness centers and posted on social media. The front of the card MUST look amazing - make potential participants want to pick it up and find out more information; the back of the card will have the contest details. The goal is to have people sign up for a 90 day fitness program, and most of the marketing will be with this postcard.

Target Market(s)

People that are thinking about beginning a health regiment; people who are already used to exercising and are willing to try a new supplement

Industry/Entity Type

Health And Wellness

Colors

Designer to choose colors to be used in the design.

Requirements
Must have
• Front Cover -- Must have the phrase "The Bright Harvest Renewal" and must have "$2,500 Grand Prize"; and must have "BrightHarvestRenewal.com"
Nice to have
• Design on Front; Details on Back; appeal to both men and women

```html
<!DOCTYPE html>
<html lang="en">
<head>
<meta charset="utf-8">
<title>The Bright Harvest Renewal – Postcard</title>
<link href="https://fonts.googleapis.com/css2?family=Open+Sans:wght@400;600;700;800&family=Roboto+Condensed:wght@700&display=swap" rel="stylesheet">
<style>
  :root {
    --page: #ecebe8;
    --card-dark: #2b2b2b;
    --blue: #2f6fb6;
    --blue-light: #4a8fd8;
    --blue-deep: #1d4f8f;
    --white: #ffffff;
    --silver: #c9ccd0;
    --text-soft: #e6e6e6;
    --rule: #7a7a7a;
  }
  * { box-sizing: border-box; margin: 0; padding: 0; }
  html, body { width: 1020px; height: 1200px; overflow: hidden; background: var(--page); }
  body { position: relative; font-family: "Open Sans", Arial, sans-serif; }

  .card { position: absolute; left: 228px; width: 566px; height: 437px; overflow: hidden; box-shadow: 0 4px 10px rgba(0,0,0,.25); }
  .card--front { top: 118px; background: var(--card-dark); }
  .card--back { top: 648px; background: var(--white); }

  /* Front */
  .brand { position: absolute; left: 30px; top: 40px; width: 228px; text-align: center; }
  .brand__mark { display: block; width: 30px; height: 30px; margin: 0 auto 12px; background: var(--blue); }
  .brand__name { color: var(--white); font-weight: 600; font-size: 18px; letter-spacing: 1.5px; text-transform: uppercase; }

  .headline { position: absolute; left: 20px; top: 138px; width: 248px; text-align: center; color: var(--white); font-weight: 800; text-transform: uppercase; line-height: 1.12; }
  .headline__top { display: block; font-size: 33px; }
  .headline__bottom { display: block; font-size: 22px; }

  .prize { position: absolute; left: 30px; top: 232px; width: 228px; height: 130px; border-radius: 4px;
    background: radial-gradient(ellipse at 50% 40%, var(--blue-light), var(--blue-deep) 80%);
    color: var(--white); font-family: "Roboto Condensed", "Arial Narrow", sans-serif; font-weight: 700; text-align: center; padding-top: 14px; }
  .prize__amount { display: block; font-size: 58px; line-height: 1; }
  .prize__label { display: block; font-size: 34px; line-height: 1.2; }

  .photo { position: absolute; inset: 0; width: 566px; height: 437px; }

  .web-band { position: absolute; left: 0; top: 400px; width: 330px; height: 37px; }
  .web-band__text { position: absolute; left: 26px; top: 400px; height: 37px; display: flex; align-items: center; gap: 11px; color: var(--white); font-weight: 700; font-size: 13px; white-space: nowrap; }

  /* Back */
  .details { position: absolute; left: 0; top: 0; width: 318px; height: 437px; background: var(--card-dark); color: var(--text-soft); }
  .details__intro { position: absolute; left: 13px; top: 20px; width: 296px; font-size: 12.5px; line-height: 1.45; }
  .details__intro p + p { margin-top: 14px; }
  .benefits { position: absolute; left: 13px; top: 136px; list-style: none; font-size: 12.5px; line-height: 17.6px; }
  .benefits li { display: flex; align-items: center; gap: 14px; }
  .benefits svg { width: 11px; height: 11px; }

  .deadline { position: absolute; left: 0; top: 304px; width: 318px; height: 90px; background: var(--blue); color: var(--white); padding: 8px 11px; font-size: 10.5px; line-height: 1.6; white-space: nowrap; letter-spacing: -0.1px; }
  .deadline strong { font-weight: 700; }
  .contact { display: flex; align-items: center; gap: 9px; font-weight: 700; font-size: 11px; }
  .contact__icon { width: 13px; height: 13px; border-radius: 50%; background: var(--white); display: inline-flex; align-items: center; justify-content: center; }

  .stamp-box { position: absolute; left: 466px; top: 22px; width: 83px; height: 75px; border: 1px solid var(--rule); }
  .address-line { position: absolute; left: 345px; width: 202px; border-top: 1px solid var(--rule); }
  .address-line--1 { top: 259px; }
  .address-line--2 { top: 295px; }
  .address-line--3 { top: 331px; }
</style>
</head>
<body>

<section class="card card--front" aria-label="Postcard front">
  <div class="brand">
    <span class="brand__mark"></span>
    <span class="brand__name">Keystone Row</span>
  </div>

  <h1 class="headline">
    <span class="headline__top">The Bright</span>
    <span class="headline__bottom">Harvest Renewal</span>
  </h1>

  <div class="prize">
    <span class="prize__amount">$2,500</span>
    <span class="prize__label">GRAND PRIZE</span>
  </div>

  <svg class="photo" viewBox="0 0 566 437">
    <defs>
      <linearGradient id="photoTones" x1="0" y1="0" x2="0" y2="1">
        <stop offset="0" stop-color="#7da25a"/>
        <stop offset=".5" stop-color="#5f8a3c"/>
        <stop offset=".72" stop-color="#8d6a5e"/>
        <stop offset="1" stop-color="#9a5a55"/>
      </linearGradient>
    </defs>
    <polygon points="482,0 566,0 566,437 448,437 278,220" fill="#b8bcc1"/>
    <polygon role="img" aria-label="Photo of a man jogging on a red running track lined with green trees"
      points="492,0 566,0 566,437 458,437 290,220" fill="url(#photoTones)"/>
  </svg>

  <svg class="web-band" viewBox="0 0 330 37" aria-hidden="true">
    <polygon points="0,0 302,0 330,37 0,37" fill="var(--white)"/>
    <polygon points="0,0 294,0 320,37 0,37" fill="var(--blue)"/>
  </svg>
  <div class="web-band__text">
    <svg width="14" height="14" viewBox="0 0 14 14" aria-hidden="true"><circle cx="7" cy="7" r="6" fill="none" stroke="#fff" stroke-width="1.3"/><ellipse cx="7" cy="7" rx="2.6" ry="6" fill="none" stroke="#fff" stroke-width="1.1"/><line x1="1" y1="7" x2="13" y2="7" stroke="#fff" stroke-width="1.1"/></svg>
    <span>www.BrightHarvestRenewal.com</span>
  </div>
</section>

<section class="card card--back" aria-label="Postcard back">
  <div class="details">
    <div class="details__intro">
      <p>The Bright Harvest Renewal has one mission – to help people be a better version of themselves.</p>
      <p>Join us in The Bright Harvest Renewal and experience some of the benefits that countless others have seen:</p>
    </div>
    <ul class="benefits">
      <li><svg viewBox="0 0 11 11"><path d="M1 6 L4 9 L10 1.5" fill="none" stroke="#fff" stroke-width="1.5"/></svg>Better health</li>
      <li><svg viewBox="0 0 11 11"><path d="M1 6 L4 9 L10 1.5" fill="none" stroke="#fff" stroke-width="1.5"/></svg>Appetite suppression</li>
      <li><svg viewBox="0 0 11 11"><path d="M1 6 L4 9 L10 1.5" fill="none" stroke="#fff" stroke-width="1.5"/></svg>Better energy</li>
      <li><svg viewBox="0 0 11 11"><path d="M1 6 L4 9 L10 1.5" fill="none" stroke="#fff" stroke-width="1.5"/></svg>Fat Loss</li>
      <li><svg viewBox="0 0 11 11"><path d="M1 6 L4 9 L10 1.5" fill="none" stroke="#fff" stroke-width="1.5"/></svg>Better focus</li>
      <li><svg viewBox="0 0 11 11"><path d="M1 6 L4 9 L10 1.5" fill="none" stroke="#fff" stroke-width="1.5"/></svg>Increased awareness</li>
      <li><svg viewBox="0 0 11 11"><path d="M1 6 L4 9 L10 1.5" fill="none" stroke="#fff" stroke-width="1.5"/></svg>Better mood</li>
      <li><svg viewBox="0 0 11 11"><path d="M1 6 L4 9 L10 1.5" fill="none" stroke="#fff" stroke-width="1.5"/></svg>Muscle preservation</li>
      <li><svg viewBox="0 0 11 11"><path d="M1 6 L4 9 L10 1.5" fill="none" stroke="#fff" stroke-width="1.5"/></svg>Better sleep</li>
    </ul>
    <div class="deadline">
      <div>Challenge Deadline: Register by <strong>October 31, 2017</strong></div>
      <div>For Challenge details, email one of our sponsors at</div>
      <div class="contact"><span class="contact__icon"><svg width="8" height="6" viewBox="0 0 8 6"><rect x=".5" y=".5" width="7" height="5" fill="none" stroke="#2f6fb6"/><path d="M.5 .5 L4 3.5 L7.5 .5" fill="none" stroke="#2f6fb6"/></svg></span>Info@KeystoneRowLaw.org</div>
      <div class="contact"><span class="contact__icon"><svg width="10" height="10" viewBox="0 0 10 10"><circle cx="5" cy="5" r="4" fill="none" stroke="#2f6fb6"/><line x1="1" y1="5" x2="9" y2="5" stroke="#2f6fb6"/><ellipse cx="5" cy="5" rx="1.8" ry="4" fill="none" stroke="#2f6fb6"/></svg></span>www.BrightHarvestRenewal.com</div>
    </div>
  </div>

  <div class="stamp-box"></div>
  <div class="address-line address-line--1"></div>
  <div class="address-line address-line--2"></div>
  <div class="address-line address-line--3"></div>
</section>

</body>
</html>
```